Wood Fired Pizza business needs a business card design

We need a business car design for a new company based in Texas called "Crusta Elm" a play off of Brindle Fen. We hand craft pizzas and cook them in our wood fired oven at temp. that reach 900 degrease, allowing the pizza to cook in 90 sec. Our customer base is private catering, festivals, and farmers markets. We would like to see designs that follow the Brindle Fen brand of Camoflauge, and Orange text. The final design should communicate pizza cooked in a wood fired oven.

```html
<!DOCTYPE html>
<html lang="en">
<head>
<meta charset="utf-8">
<title>Crusta Elm – Business Card</title>
<link rel="stylesheet" href="https://fonts.googleapis.com/css2?family=Questrial&display=swap">
<style>
  :root {
    --page-bg: #e9e4dc;
    --card-brown: #7a5a45;
    --card-brown-dark: #6b4e3b;
    --camo-green: #3f6b3c;
    --camo-olive: #6d7a4f;
    --camo-sand: #c9c6b0;
    --camo-navy: #1f2f4d;
    --badge-maroon: #4a1d1f;
    --text-orange: #e8772a;
  }
  * { margin: 0; padding: 0; box-sizing: border-box; }
  html, body {
    width: 1200px;
    height: 1000px;
    overflow: hidden;
    background: var(--page-bg);
    font-family: "Questrial", "Century Gothic", sans-serif;
  }
  .canvas {
    position: relative;
    width: 1200px;
    height: 1000px;
    display: flex;
    align-items: center;
    justify-content: center;
  }
  .business-card {
    position: relative;
    width: 1050px;
    height: 600px;
    border-radius: 6px;
    overflow: hidden;
    box-shadow: 0 10px 30px rgba(0,0,0,0.25);
  }
  .camo-border {
    position: absolute;
    inset: 0;
    background: linear-gradient(135deg,
      var(--camo-green) 0%, var(--camo-olive) 25%, var(--camo-sand) 45%,
      var(--camo-navy) 60%, var(--camo-green) 80%, var(--camo-olive) 100%);
  }
  .card-field {
    position: absolute;
    inset: 38px;
    background: linear-gradient(160deg, var(--card-brown) 0%, var(--card-brown-dark) 100%);
    border-radius: 3px;
  }
  .brand-badge {
    position: absolute;
    left: 50%;
    top: 70px;
    transform: translateX(-50%);
    width: 290px;
    height: 290px;
    border-radius: 50%;
    background: var(--badge-maroon);
    display: flex;
    align-items: center;
    justify-content: center;
  }
  .brand-name {
    color: var(--text-orange);
    font-size: 44px;
    letter-spacing: 0.5px;
  }
  .address {
    position: absolute;
    right: 90px;
    top: 110px;
    text-align: right;
    color: var(--text-orange);
    font-size: 26px;
    line-height: 1.35;
  }
  .contact {
    position: absolute;
    left: 90px;
    bottom: 90px;
    color: var(--text-orange);
  }
  .contact-name {
    font-size: 40px;
    margin-bottom: 10px;
  }
  .contact-phone {
    display: flex;
    align-items: center;
    gap: 10px;
    font-size: 26px;
  }
  .phone-icon { width: 22px; height: 22px; fill: var(--text-orange); }
</style>
</head>
<body>
<main class="canvas">
  <section class="business-card">
    <div class="camo-border" role="img" aria-label="Camouflage pattern border in green, sand and navy"></div>
    <div class="card-field">
      <div class="brand-badge">
        <span class="brand-name">Crusta Elm</span>
      </div>
      <address class="address" style="font-style:normal">
        4820 1/2 Cedar Ln<br>
        Austin TX, 78745
      </address>
      <div class="contact">
        <p class="contact-name">Dale Hartwell</p>
        <p class="contact-phone">
          <svg class="phone-icon" viewBox="0 0 24 24" aria-hidden="true">
            <path d="M6.6 10.8c1.4 2.8 3.8 5.1 6.6 6.6l2.2-2.2c.3-.3.7-.4 1-.2 1.1.4 2.3.6 3.6.6.6 0 1 .4 1 1V20c0 .6-.4 1-1 1C10.6 21 3 13.4 3 4c0-.6.4-1 1-1h3.5c.6 0 1 .4 1 1 0 1.3.2 2.5.6 3.6.1.3 0 .7-.2 1L6.6 10.8z"/>
          </svg>
          512-555-0147
        </p>
      </div>
    </div>
  </section>
</main>
</body>
</html>
```